Broschüre in Querformat für Immobilienmakler
Zielgruppe
Immobilienmakler - Überregional tätig - zielgerichtete Vermarktung - Zielgruppe sind Verkäufer oft ältere Menschen
Ich möchte eine Broschüre mit 12 Seiten im Querformat - Die Broschüre sollte der Website harvrenk-immobilien.example ein wenig ähneln.
Aufgabenstellung
klare Linie - schnell erklärbar und übersichtlich - logischer Aufbau - Aufmerksamkeit erwecken durch Bilder - schnelle Info für Querleser - VERTRAUEN - ehrlich und authentisch - nicht Eitel - schnelle Zurechtfindung - Serviceorientiert - Rundumsorglos Paket

```html
<!DOCTYPE html>
<html lang="de">
<head>
<meta charset="utf-8">
<title>Broschüre – Unsere Leistungen &amp; Kosten</title>
<link href="https://fonts.googleapis.com/css2?family=Open+Sans:wght@400;600&display=swap" rel="stylesheet">
<style>
  :root {
    --bg: #d8d9db;
    --paper: #fbfbfb;
    --blue-dark: #1f6fa9;
    --blue: #2a83bf;
    --blue-light: #5aaedc;
    --text: #555a60;
    --skyline: #7d8187;
  }
  * { box-sizing: border-box; margin: 0; padding: 0; }
  html, body { width: 1200px; height: 769px; overflow: hidden; }
  body {
    background: var(--bg);
    font-family: "Open Sans", sans-serif;
    color: var(--text);
    position: relative;
  }
  .spread {
    position: absolute;
    left: 40px; top: 172px;
    width: 1120px; height: 425px;
    display: flex;
    box-shadow: 0 12px 30px rgba(0,0,0,.18);
  }
  .page {
    position: relative;
    width: 560px; height: 425px;
    background: var(--paper);
    overflow: hidden;
  }
  .page--left { background: linear-gradient(to right, var(--paper) 92%, #e9e9e9); }
  .page--right { background: linear-gradient(to left, var(--paper) 92%, #e9e9e9); }
  .page-header { position: absolute; left: 0; top: 0; width: 100%; height: 44px; }
  .page-header svg { position: absolute; inset: 0; }
  .section-tab {
    position: absolute; left: 18px; top: 18px;
    color: #fff; font-size: 13px; font-weight: 600; letter-spacing: .3px;
  }
  .page-number {
    position: absolute; right: 18px; top: 8px;
    color: #fff; font-size: 8px;
  }
  .skyline {
    position: absolute; left: 0; bottom: 0; width: 100%; height: 120px;
    background: linear-gradient(to bottom, rgba(125,129,135,0) 0%, rgba(125,129,135,.25) 45%, rgba(90,94,100,.55) 100%);
  }
  .hero-photo {
    position: absolute; left: 22px; top: 52px; width: 516px; height: 190px;
    background: linear-gradient(135deg, #e9ecef 0%, #c9553a 35%, #b94a33 55%, #5d8a3a 80%, #3f6b2b 100%);
  }
  .headline {
    position: absolute; left: 30px; top: 252px; width: 510px;
    color: var(--blue-dark); font-size: 19.5px; font-weight: 400;
  }
  .intro {
    position: absolute; left: 30px; width: 500px;
    font-size: 10.5px; line-height: 1.5;
  }
  .page--left .intro { top: 286px; }
  .page--right .intro { top: 56px; font-size: 10px; width: 520px; left: 22px; }
  .schedule {
    position: absolute; left: 60px; top: 120px; width: 440px;
    display: grid; grid-template-columns: 1fr auto; column-gap: 30px;
    font-size: 11px; line-height: 17.5px;
  }
  .schedule h2 {
    color: var(--blue); font-size: 13.5px; font-weight: 600; margin-bottom: 4px;
  }
  .schedule ul { list-style: none; }
  .schedule .timing { text-align: right; }
</style>
</head>
<body>
  <main class="spread">
    <section class="page page--left">
      <header class="page-header">
        <svg width="560" height="44" viewBox="0 0 560 44">
          <defs>
            <linearGradient id="bandL" x1="0" x2="1">
              <stop offset="0" stop-color="#1f6fa9"/>
              <stop offset="1" stop-color="#5aaedc"/>
            </linearGradient>
          </defs>
          <polygon points="0,12 560,6 560,18 200,22 0,24" fill="url(#bandL)"/>
          <polygon points="0,12 175,12 190,22 175,40 0,40" fill="#1f6fa9"/>
        </svg>
        <span class="section-tab">Unsere Leistungen</span>
        <span class="page-number">05</span>
      </header>
      <div class="skyline" role="img" aria-label="Graue Stadtsilhouette als Fußleiste"></div>
      <div class="hero-photo" role="img" aria-label="Foto eines roten Holzhauses mit Ziegeldach und grünem Garten"></div>
      <h1 class="headline">Unsere Leistungen als Immobilienmakler für Sie:</h1>
      <p class="intro">Mit der Aufstellung soll gezeigt werden, was wir „Team Harvrenk-Immobilien“ als qualifizierte Immobilienmakler für Sie erbringen. Wir gehen mit sämtlichen Leistungen in Vorleistung und werden nur bei einem erfolgreichen Kaufvertragsabschluss mit einer Provision honoriert.</p>
    </section>

    <section class="page page--right">
      <header class="page-header">
        <svg width="560" height="44" viewBox="0 0 560 44">
          <defs>
            <linearGradient id="bandR" x1="0" x2="1">
              <stop offset="0" stop-color="#1f6fa9"/>
              <stop offset="1" stop-color="#5aaedc"/>
            </linearGradient>
          </defs>
          <polygon points="0,12 560,4 560,18 200,24 0,26" fill="url(#bandR)"/>
          <polygon points="0,12 95,12 110,22 95,40 0,40" fill="#1f6fa9"/>
        </svg>
        <span class="section-tab">Kosten</span>
        <span class="page-number">06</span>
      </header>
      <div class="skyline" role="img" aria-label="Graue Stadtsilhouette als Fußleiste"></div>
      <p class="intro">Unser Service in sämtlichen Phasen ist bei einem Vermarktungsauftrag mit der vereinbarten Provision abgegolten. Es entstehen Ihnen keine Mehrkosten. Wir verlangen keine Vorauszahlungen und es ist für uns eine Selbstverständlichkeit, dass wir erst nach erfolgreicher Vermittlung Ihrer Immobilie unserer Leistung in Rechnung stellen.</p>
      <div class="schedule">
        <div>
          <h2>Leistung:</h2>
          <ul>
            <li>Wertermittlung</li>
            <li>Marktanalyse</li>
            <li>Erstellung des professionellen Expose</li>
            <li>Nachbearbeitung Fotos</li>
            <li>360° VR erstellen</li>
            <li>Vermarktungsbeginn</li>
            <li>Info an vorgemerkte Interessenten</li>
            <li>Erreichbarkeit</li>
            <li>Finanzierungsangebote</li>
            <li>Veröffentlichung Homepage</li>
            <li>Erstellung Energieausweis</li>
          </ul>
        </div>
        <div class="timing">
          <h2>Zeitplan der Ausführung:</h2>
          <ul>
            <li>maximal 3 Werktage</li>
            <li>maximal 3 Werktage</li>
            <li>4 Werktage</li>
            <li>3 Werktage</li>
            <li>3 Werktage</li>
            <li>maximal 4 Werktage</li>
            <li>maximal 3 Werktage</li>
            <li>täglich</li>
            <li>4 Werktage</li>
            <li>5 Werktage</li>
            <li>2 Werktage</li>
          </ul>
        </div>
      </div>
    </section>
  </main>
</body>
</html>
```